Buch-/E-Book-Cover für Roman
Der Designer arbeitet trotz des sicher nicht unerheblichen Arbeitsaufwands schnell, ist unermüdlich und hat ein Auge für Details. Kundenwünsche und Änderungen setzt er ohne Zögern um. Der Kontakt war jederzeit von Höflichkeit geprägt. Ich kommen jeder Zeit gerne wieder auf ihn zurück.
Aufgabenstellung
Ich suche für meinen Roman ein Cover für das Taschenbuch und das eBook.
Bei dem Roman handelt es sich um eine Mischung aus biografischem Roman und Thriller, und das sollte sich im Cover widerspiegeln.
Autor: Matthias Brandtstätter
Titel: Kalte Nachbarn
Untertitel: Das Tagebuch eines Entführers
Klappentext:
»Ich schaue ins Gesicht eines Toten und erahne mein Schicksal.«
Der Journalist Konrad Velde ist in die Fänge eines Serienmörders geraten. Torlak hat zahlreiche Männer heimtückisch erdrosselt. Um dem sicheren Tod zu entgehen, greift Konrad zu einer List und überredet Torlak, dessen Lebensgeschichte aufzuschreiben. Konrad taucht in prägende Kindheitserinnerungen ein, hört intime Geständnisse und erfährt von der zunehmenden Veränderung Torlaks.
Beide Männer begeben sich in dunkle Abgründe, in einer Nacht mit ungewissem Ausgang.
Ich stelle mir einen gefesselten Stuhl vor, im Hintergrund evtl. schattenhafte Umrisse, doch das überlasse ich dem geschulten Auge des Illustrators. Für bessere Ideen bin ich selbstverständlich offen.
Um eine genauere Vorstellung des Romans zu vermitteln, möchte ich weitere Informationen mitgeben:
Beide Männer, der Mörder und der Journalist (an einen Stuhl gefesselt), sitzen sich gegenüber, während der Mörder seine Lebensgeschichte erzählt. Der Mörder ist homosexuell und hat eine nekrophile Neigung (derlei eventuelle Einflüsse im Cover nur dezent darstellen) und erwürgt seine männlichen Opfer zumeist mit einer Krawatte. Es geht um eine differenzierte Darstellung des Mörders, um das Spannungsfeld zwischen positiven und negativen Impulsen.
Eine Textdatei mit den relevanten Informationen liegt bei. Designvorlage mit den richtigen Maßen ist bei Interesse als PNG-Datei vorhanden. Das Cover für das Taschenbuch sollte als PDF mit mind. 300 dpi vorliegen und möglichst nicht großer als 40MB sein (Empfehlung von Buchfalter). Das Cover für das eBook benötige ich in..

```html
<!DOCTYPE html>
<html lang="de">
<head>
<meta charset="utf-8">
<title>Kalte Nachbarn – Buchumschlag</title>
<link rel="stylesheet" href="https://fonts.googleapis.com/css2?family=Cinzel:wght@400;700&family=Source+Sans+3:wght@400;700&display=swap">
<style>
  :root {
    --ink: #050505;
    --blood: #e0121b;
    --paper: #f2f2f2;
    --shadow-wall: #1d1c17;
    --chair-red: #c42a1f;
    --chair-wood: #b9772f;
    --floor-grey: #5e5b54;
  }
  * { margin: 0; padding: 0; box-sizing: border-box; }
  html, body { width: 1200px; height: 860px; overflow: hidden; background: var(--ink); }
  .cover-wrap {
    position: relative; width: 1200px; height: 860px;
    background: var(--ink); color: var(--paper); overflow: hidden;
  }
  .back-cover {
    position: absolute; left: 0; top: 0; width: 573px; height: 860px;
    background: radial-gradient(ellipse 300px 260px at 290px 230px, var(--shadow-wall) 0%, rgba(20,20,16,0.6) 55%, var(--ink) 100%);
  }
  .spine { position: absolute; left: 573px; top: 0; width: 44px; height: 860px; }
  .front-cover {
    position: absolute; left: 617px; top: 0; width: 583px; height: 860px;
    background: radial-gradient(ellipse 320px 300px at 320px 620px, #262420 0%, #111010 60%, var(--ink) 100%);
  }
  .title {
    font-family: "Cinzel", serif; font-weight: 700; color: var(--blood);
    text-align: right; line-height: 1; white-space: nowrap;
  }
  .subtitle {
    font-family: "Cinzel", serif; font-weight: 400; color: var(--paper);
    text-align: right; white-space: nowrap; letter-spacing: 0.02em;
  }
  .back-cover .title-main { position: absolute; left: 150px; top: 118px; width: 275px; font-size: 74px; }
  .back-cover .title-sub  { position: absolute; left: 150px; top: 210px; width: 275px; font-size: 44px; }
  .back-cover .subtitle   { position: absolute; left: 150px; top: 268px; width: 275px; font-size: 15.5px; }
  .blurb { position: absolute; left: 123px; top: 328px; width: 335px; font-family: "Source Sans 3", sans-serif; }
  .blurb-quote { color: var(--blood); font-weight: 700; font-size: 15px; line-height: 19px; margin-bottom: 19px; }
  .blurb p { font-size: 14.6px; line-height: 18.6px; text-align: justify; hyphens: auto; margin-bottom: 18px; }
  .barcode-space { position: absolute; left: 361px; top: 715px; width: 182px; height: 110px; background: #fff; }
  .spine-text {
    position: absolute; left: 33px; top: 46px; transform-origin: 0 0; transform: rotate(90deg);
    font-family: "Cinzel", serif; font-size: 18px; white-space: nowrap; letter-spacing: 0.03em;
  }
  .spine-author { color: var(--paper); }
  .spine-title { color: var(--blood); margin: 0 12px; }
  .spine-subtitle { color: var(--paper); font-size: 16px; letter-spacing: 0.07em; }
  .front-cover .title-main { position: absolute; left: 105px; top: 36px; width: 372px; font-size: 102px; }
  .front-cover .title-sub  { position: absolute; left: 105px; top: 160px; width: 372px; font-size: 60px; }
  .front-cover .subtitle   { position: absolute; left: 105px; top: 237px; width: 372px; font-size: 20.5px; }
  .scene-image { position: absolute; left: 130px; top: 272px; width: 400px; height: 530px; }
  .author-name {
    position: absolute; left: 95px; top: 786px; width: 382px; text-align: right;
    font-family: "Cinzel", serif; font-size: 26px; color: var(--paper); white-space: nowrap; letter-spacing: 0.02em;
  }
</style>
</head>
<body>
<main class="cover-wrap">
  <section class="back-cover">
    <div class="title title-main">KALTE</div>
    <div class="title title-sub">NACHBARN</div>
    <div class="subtitle">Das Tagebuch eines Entführers</div>
    <div class="blurb">
      <div class="blurb-quote">»Ich schaue ins Gesicht eines Toten und erahne mein Schicksal.«</div>
      <p>Der Journalist Konrad Velde ist in die Fänge eines Serienmörders geraten. Torlak hat zahlreiche Männer heimtückisch erdrosselt. Um dem sicheren Tod zu entgehen, greift Konrad zu einer List und überredet Torlak, dessen Lebensgeschichte aufzuschreiben. Konrad taucht in prägende Kindheitserinnerungen ein, hört intime Geständnisse und erfährt von der zunehmenden Veränderung Torlaks.</p>
      <p>Beide Männer begeben sich in dunkle Abgründe, in einer Nacht mit ungewissem Ausgang.</p>
    </div>
    <div class="barcode-space"></div>
  </section>

  <section class="spine">
    <div class="spine-text">
      <span class="spine-author">MATTHIAS BRANDTSTÄTTER</span><span class="spine-title">KALTE NACHBARN</span><span class="spine-subtitle">DAS TAGEBUCH EINES ENTFÜHRERS</span>
    </div>
  </section>

  <section class="front-cover">
    <div class="title title-main">KALTE</div>
    <div class="title title-sub">NACHBARN</div>
    <div class="subtitle">Das Tagebuch eines Entführers</div>
    <svg class="scene-image" role="img" aria-label="Foto: Holzstuhl mit roter Sitzfläche im Lichtkegel, davor ein zusammengerolltes Seil auf dunklem Dielenboden" viewBox="0 0 400 530" preserveAspectRatio="none">
      <defs>
        <radialGradient id="sceneTones" cx="0.5" cy="0.52" r="0.55" fx="0.5" fy="0.45">
          <stop offset="0" stop-color="var(--chair-red)"/>
          <stop offset="0.3" stop-color="#a4391f"/>
          <stop offset="0.55" stop-color="var(--chair-wood)" stop-opacity="0.75"/>
          <stop offset="0.8" stop-color="var(--floor-grey)" stop-opacity="0.5"/>
          <stop offset="1" stop-color="var(--ink)" stop-opacity="0"/>
        </radialGradient>
      </defs>
      <rect width="400" height="530" fill="url(#sceneTones)"/>
    </svg>
    <div class="author-name">MATTHIAS BRANDTSTÄTTER</div>
  </section>
</main>
</body>
</html>
```